Payment Processor Website Design

Our company LumaPort, an online processor of payments is seeking talented submissions for our website redesign. The winning design will be chopped up and converted into a WordPress theme to allow for easy content additions and updates.

We are looking for modern designs that rival current websites in our industry (qindle.example, ploverbank.example, zunmo.example, kelvory.example, mossfieldcharges.example, harrowlinecharges.example, TuxCoin.example).

Our company is seeking to expand our reach to software developers and engineers who are either integrating our payment platform into their offerings or are engineering a custom solution for the company they work for and are in need of a payment platform such as our own.

We currently work with hundreds of different business partners whom either resell our services or integrate our processing capabilities into their software (which they sell). We also must communicate effectively to end users, businesses, who seek us out directly for their payment processing needs.

We are open to different color schemes but would ultimately like them to be somewhat inline with our current logo (see attached). Our website needs to instill security and confidence to any current and/or potential user as we are trusted with private and sensitive information.

We are seeking submissions from qualified; individual freelancers, freelance teams, and agencies who can attack this project in its entirety. Since this project is a total redesign, we would like submissions that have the capability to design any custom graphics, icons, buttons, and illustrations in line with our industry, capabilities, offerings, and content. We are looking for someone to design our new website and would prefer a vendor who can also help us to design elements (graphics, illustrations, charts, workflows) within our website.

Designs will be converted into a wordpress theme and we would like to utilize widgets for as many areas as possible to make editing and updating easy.

We are seeking the creation of a few unique pages but many of the pages for the majority of our content will just be internal content pages which will be duplicated.

We will likely contract with the winning submission for future work.

Please see Design Reference Document for more information

Target Market(s)

Resellers
Merchant Service Providers
Software Developers
Independent Sales Organizations (ISOs)
App Builders
Mobile App Builders
Independent Software Developers
Organizational Software Developers
Businesses who need to accept payments
Governments
Municipalities
Schools
DMVs
Courts
Retailers
Medical Offices
Hosipitals
Clinics
Dr. Offices
Gyms
Churches
Non-Profits
Software Companies
Technology Companies
Startups

Industry/Entity Type

Industry

Requirements
Should not have
• Logo cannot change drastically.

```html
<!DOCTYPE html>
<html lang="en">
<head>
<meta charset="utf-8">
<title>LumaPort — Payment Processing</title>
<link rel="stylesheet" href="https://fonts.googleapis.com/css2?family=Arimo:wght@400;700&family=Source+Sans+3:wght@400;600&family=Open+Sans:wght@400;700&display=swap">
<style>
:root{
  --topbar:#ebebeb;
  --ink:#222;
  --link-blue:#33339a;
  --welcome:#3b3bb5;
  --violet:#6769c4;
  --red:#e0282e;
  --red-dark:#b81c22;
  --pink-ring:#f1a3a3;
  --section-gray:#f1f1f1;
  --footer:#32373a;
  --footer-text:#e8e8e8;
  --nav-text:#333;
}
*{margin:0;padding:0;box-sizing:border-box}
html,body{width:1200px;height:998px;overflow:hidden}
body{position:relative;background:#fff;font-family:"Arimo",Arial,sans-serif;color:var(--ink)}
.abs{position:absolute}

/* top bar */
.topbar{left:0;top:0;width:1200px;height:42px;background:var(--topbar)}
.brand{left:312px;top:11px;font-family:"Source Sans 3",sans-serif;font-size:15px;font-weight:600;color:var(--link-blue);display:flex;align-items:center;gap:4px}
.brand i{width:7px;height:7px;background:var(--red);border-radius:50%;display:block}
.toplinks{right:402px;top:16px;font-size:6.4px;line-height:8px;color:var(--link-blue);display:flex;gap:7px;white-space:nowrap}
.search{left:820px;top:15px;display:flex}
.search .field{width:42px;height:9px;background:#fff;border:1px solid #ccc}
.search .btn{width:25px;height:9px;background:var(--link-blue);color:#fff;font-size:6px;text-align:center;line-height:9px}

/* hero */
.hero{left:0;top:42px;width:1200px;height:214px;background:linear-gradient(90deg,#0d6b3a 0%,#2c8a77 10%,#a9c3e6 20%,#c9dbf3 40%,#b8d1f2 60%,#a8c6ef 80%,#2f8fd6 88%,#44b9c1 100%)}
.hero-glow{left:220px;top:42px;width:770px;height:214px;background:radial-gradient(ellipse at 25% 85%,rgba(150,180,70,.55),transparent 45%),radial-gradient(ellipse at 75% 90%,rgba(70,90,200,.45),transparent 45%),radial-gradient(ellipse at 45% 110%,rgba(220,80,160,.4),transparent 35%)}
.badge{width:66px;height:66px;border-radius:50%;background:var(--red);border:3px solid #c21d24;box-shadow:0 0 0 2px rgba(255,255,255,.35)}
.badge.business{left:402px;top:66px}
.badge.developer{left:719px;top:66px}
.or{left:571px;top:134px;width:55px;height:55px;border-radius:50%;background:var(--violet);color:#fff;font-family:"Source Sans 3",sans-serif;font-size:17px;line-height:55px;text-align:center}
.audience{font-family:"Source Sans 3",sans-serif;font-size:38px;line-height:1;width:260px;text-align:center}
.audience.business{left:305px;top:142px;color:#f7f3a2}
.audience.developer{left:628px;top:142px;color:#fff}
.cta{height:27px;width:134px;background:linear-gradient(#ec3a3f,var(--red-dark));color:#fff;font-family:"Source Sans 3",sans-serif;font-size:13px;text-align:center;line-height:27px;border-radius:2px;box-shadow:0 1px 2px rgba(0,0,0,.3)}
.cta.business{left:370px;top:198px}
.cta.developer{left:689px;top:198px}

/* nav */
.mainnav{left:0;top:256px;width:1200px;height:34px;border-bottom:2px solid #ddd;display:flex;justify-content:center;align-items:center}
.mainnav span{font-size:8.6px;color:var(--nav-text);letter-spacing:.2px;padding:0 4px;white-space:nowrap}
.nav-marker{left:455px;top:285px;width:11px;height:6px;border-radius:6px 6px 0 0;background:#2c5b8a}

/* welcome */
.welcome-title{left:312px;top:320px;font-size:21px;color:var(--welcome)}
.welcome-text{left:312px;top:355px;width:372px;font-size:8.4px;line-height:10.9px;color:#222}
.industries{left:714px;top:311px;width:174px;height:182px;background:var(--violet);border-radius:12px}
.industries h3{position:absolute;left:0;top:13px;width:174px;text-align:center;color:#fff;font-size:8.4px;font-weight:700}
.industries ul{position:absolute;left:16px;top:37px;width:142px;height:133px;background:#fff;border-radius:10px;list-style:none;padding-top:1px}
.industries li{height:21.6px;display:flex;align-items:center;font-size:8.5px;color:#222;padding-left:16px;gap:15px;white-space:nowrap}
.industries svg{width:9px;height:9px;flex:none}

/* ACH */
.ach{left:0;top:518px;width:1200px;height:278px;background:var(--section-gray)}
.ach-title{left:0;top:541px;width:1200px;text-align:center;font-size:18px;font-weight:700;color:#333}
.ring{width:88px;height:84px}
.feature-title{width:200px;text-align:center;font-size:11px;line-height:14px;color:#555}
.feature-text{width:132px;font-size:7.4px;line-height:11px;color:#666}

/* footer */
.footer{left:0;top:796px;width:1200px;height:202px;background:var(--footer)}
.footer-logo{left:312px;top:851px;width:106px;height:60px;background:#1d1f20;border-radius:3px;padding:4px}
.footer-logo div{width:100%;height:100%;background:#fff;display:flex;align-items:center;justify-content:center;font-family:"Source Sans 3",sans-serif;font-weight:600;font-size:17px;color:var(--link-blue);gap:4px}
.footer-logo i{width:7px;height:7px;background:var(--red);border-radius:50%;display:block}
.fcol{font-family:"Open Sans",sans-serif;color:var(--footer-text)}
.fcol h4{font-size:6.5px;font-weight:700;letter-spacing:.3px;margin-bottom:4px}
.fcol p{font-size:7px;line-height:11px}
.fcol .small{font-size:5.6px;line-height:7px;margin-bottom:7px}
.fcol a{color:#2f8fc6;text-decoration:none}
.social{left:760px;top:839px;display:flex;gap:6px}
.social span{width:12px;height:12px;background:#f2f2f2;border-radius:1px;display:block}
</style>
</head>
<body>
<header>
  <div class="abs topbar"></div>
  <div class="abs brand"><span>LumaPort</span><i></i></div>
  <nav class="abs toplinks"><span>CALL US ON: 555 010 2284</span><span>EMAIL US</span><span>LOGIN</span></nav>
  <div class="abs search"><div class="field"></div><div class="btn">search</div></div>
</header>

<section>
  <div class="abs hero" role="img" aria-label="Soft blurred photo of colourful umbrellas against a blue sky"></div>
  <div class="abs hero-glow"></div>
  <div class="abs badge business" role="img" aria-label="Icon for business users"></div>
  <div class="abs badge developer" role="img" aria-label="Puzzle piece icon for developers"></div>
  <div class="abs or">OR</div>
  <div class="abs audience business">Business</div>
  <div class="abs audience developer">Developer</div>
  <div class="abs cta business">I HAVE A BUSINESS</div>
  <div class="abs cta developer">I AM DEVELOPER</div>
</section>

<nav class="abs mainnav">
  <span>SOLUTIONS</span><span>DEVELOPERS</span><span>PARTNERS</span><span>COMPANY</span><span>RESOURCES</span><span>BLOG</span>
</nav>
<div class="abs nav-marker"></div>

<main>
  <h1 class="abs welcome-title" style="font-weight:400">Welcome</h1>
  <p class="abs welcome-text">Jujubes jelly beans pastry cake biscuit jujubes cheesecake. Chocolate bar chocolate bar topping lemon drops tootsie roll. Macaroon chocolate bar sweet tart powder tootsie roll macaroon liquorice. Bonbon carrot cake tart. Danish dessert danish croissant topping biscuit. Candy lollipop lemon drops tart muffin bear claw gummi bears softwear.example carrot cake.<br>Carrot cake carrot cake croissant tiramisu. Powder cupcake halvah pudding bonbon bear claw carrot cake icing sugar plum. Lollipop cake muffin dessert gummies biscuit oat cake jujubes.<br>Oat cake sugar plum icing cotton candy pastry gummi bears. Chupa chups jujubes cotton candy. Cotton candy icing dessert.<br>Topping topping caramels lemon drops lollipop dragée chocolate cake cookie. Tiramisu jujubes cake gummies icing dessert sweet roll sesame snaps. Liquorice caramels cookie.</p>

  <aside class="abs industries">
    <h3>CUSTOM INDUSTRY SOLUTIONS</h3>
    <ul>
      <li><svg viewBox="0 0 10 10"><path d="M1 5.5 4 8.5 9 1.5" fill="none" stroke="#3b3b9a" stroke-width="2"/></svg>Governement</li>
      <li><svg viewBox="0 0 10 10"><path d="M1 5.5 4 8.5 9 1.5" fill="none" stroke="#3b3b9a" stroke-width="2"/></svg>Medical</li>
      <li><svg viewBox="0 0 10 10"><path d="M1 5.5 4 8.5 9 1.5" fill="none" stroke="#3b3b9a" stroke-width="2"/></svg>Fitness</li>
      <li><svg viewBox="0 0 10 10"><path d="M1 5.5 4 8.5 9 1.5" fill="none" stroke="#3b3b9a" stroke-width="2"/></svg>Martial Arts</li>
      <li><svg viewBox="0 0 10 10"><path d="M1 5.5 4 8.5 9 1.5" fill="none" stroke="#3b3b9a" stroke-width="2"/></svg>Alarm monitoring</li>
      <li><svg viewBox="0 0 10 10"><path d="M1 5.5 4 8.5 9 1.5" fill="none" stroke="#3b3b9a" stroke-width="2"/></svg>Property management</li>
    </ul>
  </aside>

  <section>
    <div class="abs ach"></div>
    <h2 class="abs ach-title">ACH Payment processing</h2>

    <svg class="abs ring" style="left:336px;top:585px" viewBox="0 0 88 84">
      <circle cx="44" cy="42" r="40" fill="none" stroke="var(--pink-ring)" stroke-width="2.5"/>
      <g fill="var(--red)">
        <rect x="16" y="26" width="42" height="26"/>
        <rect x="58" y="26" width="16" height="30" transform="skewX(-4)"/>
      </g>
      <g stroke="#fff" stroke-width="1">
        <line x1="16" y1="38" x2="58" y2="38"/><line x1="16" y1="43" x2="58" y2="43"/><line x1="16" y1="48" x2="58" y2="48"/>
        <line x1="60" y1="36" x2="72" y2="36"/><line x1="60" y1="41" x2="72" y2="41"/><line x1="60" y1="46" x2="72" y2="46"/>
      </g>
    </svg>
    <svg class="abs ring" style="left:552px;top:585px" viewBox="0 0 88 84">
      <circle cx="44" cy="42" r="40" fill="none" stroke="var(--pink-ring)" stroke-width="2.5"/>
      <circle cx="44" cy="42" r="21" fill="none" stroke="var(--red)" stroke-width="5"/>
      <circle cx="44" cy="42" r="7" fill="none" stroke="var(--red)" stroke-width="3.5"/>
      <g stroke="var(--red)" stroke-width="5"><line x1="44" y1="12" x2="44" y2="30"/><line x1="44" y1="54" x2="44" y2="72"/><line x1="14" y1="42" x2="32" y2="42"/><line x1="56" y1="42" x2="74" y2="42"/></g>
    </svg>
    <svg class="abs ring" style="left:757px;top:585px" viewBox="0 0 88 84">
      <circle cx="44" cy="42" r="40" fill="none" stroke="var(--pink-ring)" stroke-width="2.5"/>
      <rect x="24" y="20" width="40" height="28" rx="2" fill="var(--red)"/>
      <rect x="28" y="24" width="32" height="20" fill="#fff"/>
      <g fill="var(--red)"><rect x="34" y="36" width="4" height="7"/><rect x="40" y="32" width="4" height="11"/><rect x="46" y="28" width="4" height="15"/><rect x="30" y="26" width="8" height="2"/></g>
      <path d="M16 50h56l-5 6H21z" fill="var(--red)"/>
    </svg>

    <h3 class="abs feature-title" style="left:278px;top:689px;font-weight:400">Payment Getaway</h3>
    <h3 class="abs feature-title" style="left:493px;top:689px;font-weight:400">ACH Payment API</h3>
    <h3 class="abs feature-title" style="left:702px;top:678px;font-weight:400">Processing<br>for Software Development</h3>

    <p class="abs feature-text" style="left:318px;top:717px">Jujubes jelly beans pastry cake biscuit jujubes cheesecake. Chocolate bar chocolate bar topping lemon drops toot-sie roll. Macaroon chocolate bar sweet</p>
    <p class="abs feature-text" style="left:532px;top:716px">Jujubes jelly beans pastry cake biscuit jujubes cheesecake. Chocolate bar chocolate bar topping lemon drops toot-sie roll. Macaroon chocolate bar sweet</p>
    <p class="abs feature-text" style="left:742px;top:719px">Jujubes jelly beans pastry cake biscuit jujubes cheesecake. Chocolate bar chocolate bar topping lemon drops toot-sie roll. Macaroon chocolate bar sweet</p>
  </section>
</main>

<footer>
  <div class="abs footer"></div>
  <div class="abs footer-logo"><div><span>LumaPort</span><i></i></div></div>
  <div class="abs fcol" style="left:528px;top:833px;width:140px">
    <h4>CONTACT</h4>
    <p>LumaPort<br>Address: gjgjgu 13, 9000<br>Tel.: 9999 99 999</p>
    <h4 style="margin-top:12px">UPDATES</h4>
    <p class="small">Jujubes jelly beans pastry cake biscuit jujubes cheesecake</p>
    <p class="small">Jujubes jelly beans pastry cake biscuit jujubes cheesecake</p>
  </div>
  <div class="abs social" aria-label="Social links"><span></span><span></span><span></span><span></span><span></span></div>
  <div class="abs fcol" style="left:759px;top:874px;width:152px">
    <h4>PRESS</h4>
    <p>Press and media inquiries? Please contact us<br>or <a href="#">download</a> a high resolution logo.</p>
    <h4 style="margin-top:15px">LEGAL</h4>
    <p style="font-size:6.5px">Copyright © 2014 LumaPort, All rights reserved.</p>
  </div>
</footer>
</body>
</html>
```